VELVET ORBITS - BOOK COVER

I have written a book called VELVET ORBIT - HOW TO CLIMB PAST EVERY LIMIT TO THE TOP RUNG. I need a front cover design for the book. The book cover needs to be intriguing for someone to pick it up and read the first couple of pages. I want people to think about ACHIEVING SUCCESS when they read this book.
PLEASE LOOK AT THE ATTACHMENT. THANKS!

Target Market(s)

males, entrepreneurs, small business owners, salespeople, corporate executives

Industry/Entity Type

Business

Logo Text

VELVET ORBITS

Logo styles of interest
Emblem Logo
Abstract Logo
Font styles to use
Serif
Sans Serif

Colors
ec1f27
000000
959595
ffffff

Requirements
Must have
• It has to have a "hurricane" feel to it with hurricane colors.
Nice to have
• I open to your ideas
Should not have
• no other colors except red, black, gray, white.

```html
<!DOCTYPE html>
<html lang="en">
<head>
<meta charset="utf-8">
<title>Velvet Orbit – Book Cover</title>
<link rel="stylesheet" href="https://fonts.googleapis.com/css2?family=Anton&family=Oswald:wght@500;700&display=swap">
<style>
  :root {
    --red: #ec1f27;
    --black: #000000;
    --gray: #959595;
    --mat: #d4d4d4;
    --white: #ffffff;
  }
  * { margin: 0; padding: 0; box-sizing: border-box; }
  html, body {
    width: 857px;
    height: 1200px;
    overflow: hidden;
    background: var(--mat);
  }
  .cover {
    position: absolute;
    left: 109px;
    top: 113px;
    width: 640px;
    height: 973px;
    background: var(--white);
    overflow: hidden;
  }
  .title {
    position: absolute;
    left: 0;
    width: 100%;
    text-align: center;
    font-family: "Anton", "Oswald", sans-serif;
    text-transform: uppercase;
    line-height: 1;
  }
  .title-top {
    top: 22px;
    font-size: 154px;
    letter-spacing: 2px;
    color: var(--red);
  }
  .title-bottom {
    top: 157px;
    font-size: 108px;
    letter-spacing: 1px;
    color: var(--black);
  }
  .storm-art {
    position: absolute;
    left: 20px;
    top: 272px;
    width: 600px;
    height: 430px;
    background:
      radial-gradient(ellipse 55% 40% at 50% 48%, #8f9b90 0%, #b9c1b8 45%, rgba(255,255,255,0) 80%),
      var(--white);
  }
  .subtitle {
    position: absolute;
    left: 0;
    top: 714px;
    width: 100%;
    text-align: center;
    font-family: "Oswald", sans-serif;
    font-weight: 500;
    font-size: 33px;
    line-height: 41px;
    color: var(--black);
    text-transform: uppercase;
  }
  .author-band {
    position: absolute;
    left: 34px;
    top: 832px;
    width: 572px;
    height: 113px;
    background: var(--red);
    display: flex;
    align-items: center;
    justify-content: center;
  }
  .author-name {
    font-family: "Anton", "Oswald", sans-serif;
    font-size: 78px;
    letter-spacing: 1px;
    color: var(--white);
    text-transform: uppercase;
    line-height: 1;
  }
</style>
</head>
<body>
  <main class="cover">
    <h1 class="title title-top">Velvet</h1>
    <div class="title title-bottom">Orbit</div>
    <div class="storm-art" role="img" aria-label="Swirling hurricane of dollar banknotes and coins spiralling upward"></div>
    <p class="subtitle">How to climb past every limit<br>to the top rung</p>
    <div class="author-band">
      <span class="author-name">Dale Marrow</span>
    </div>
  </main>
</body>
</html>
```